Logo & Business card - Want to paint the town?

Brushvane - Top Quality Painting & Decorating

Brushvane are a painting & decorating company who work predominantly in the residential market and not commercial. We require a logo and business cards design

The company is based Christchurch NZ. Christchurch had major earthquakes in 2010 and 2011, which devastated the city. The city is in rebuild and fixing phase and will be for the next 5 years to get the city back on it's feet. As a result of the earthquakes are a lot of homes being fixed that require painting and decorating.

Additional to the earthquake work there is also huge growth in the city meaning lots of new homes are being built to accommodate the growth.

Alongside this there is an every growing rental market, so we not only work on residential earthquake repairs and new builds but also work with real estate agents, property managers and interior designers.

Christchurch has seen a large number of tradesmen enter the market and not all of whom are qualified/skilled. Our company’s painters are those with years of experience and who pride themselves on top quality precision work.

Brushvane are about quality jobs, done to a very high level at an affordable price. We are not the cheapest but also not the most expensive. Our logo and cards must reflect the quality of our work. Brushvane requires a professional logo and business card targeted to the higher end of the residential market.

Target Market(s)

Builders requiring contract painters, housing companies such as Tom Halvick, Stalwart buildings, Ridgeway Home etc., real estate agents, property managers, interior designers and home owners.

The business cards and logo must appeal to builders, homeowner, interior designers and real estate agents so can’t be too masculine/feminine.

It needs to be bold, professional and stylish.

Industry/Entity Type

Residential

Logo Text

Brushvane

Logo styles of interest
Wordmark Logo
Requirements
Must have
• The logo and business cards must be bold, clean, modern, smart, simple, self explanatory, tidy, easy to read, timeless, and not frilly.

We are about quality, precision and being able to cut a straight line, so the card needs to avoid and curvy brush strokes as this denotes a bad a and sloppy painter.

The card and logo must scream top quality and affordability.
The card must be clean and modern, high end and stylish.

The logo must be something, which will go well on a silver/ black background as eventually as the van fleet will be either silver or black, so it must punch out on these colours.

For contact details that need to appear on the business cards see the full brief attached.
Nice to have
• One idea could be to have a picture on the business card of a well-painted stylish modern home interior, which would eventually be replaced by picture of Brushvane's paint jobs.
Should not have
• It definitely must not include is paint drips; paint pot with dribbles over the side of it, splurges of paint, or paintbrush swooshes as this indicates a messy painter.

Most colours are ok except for pink, orange or pastel colours.

```html
<!DOCTYPE html>
<html lang="en">
<head>
<meta charset="utf-8">
<title>Brushvane Business Card Options</title>
<link href="https://fonts.googleapis.com/css2?family=Overpass:ital,wght@0,400;0,800;1,400&display=swap" rel="stylesheet">
<style>
  :root {
    --backdrop: #262626;
    --card: #ffffff;
    --ink: #333333;
    --label: #ffffff;
    --sky: #a9dff4;
    --sun: #fff23a;
    --leaf: #3a8f6a;
    --ocean: #3a95c8;
    --plum: #a95a8f;
    --lime: #b8d86a;
  }
  * { margin: 0; padding: 0; box-sizing: border-box; }
  html, body { width: 1200px; height: 1000px; overflow: hidden; }
  body {
    background: var(--backdrop);
    font-family: "Overpass", Arial, sans-serif;
    color: var(--ink);
    position: relative;
  }
  .card {
    position: absolute;
    left: 252px;
    width: 708px;
    height: 404px;
    background: var(--card);
  }
  .card--classic { top: 79px; }
  .card--modern { top: 533px; height: 403px; }
  .colour-band {
    position: absolute; left: 0; top: 0; width: 708px; height: 23px;
    background: linear-gradient(90deg, var(--sky) 0%, var(--leaf) 28%, var(--ocean) 48%, var(--plum) 64%, var(--lime) 76%, var(--sun) 90%, var(--sky) 100%);
  }
  .divider { position: absolute; left: 354px; top: 87px; width: 2px; height: 280px; background: var(--ink); }
  .t { position: absolute; line-height: 1; white-space: nowrap; }
  .company { font-size: 26px; }
  .detail { font-size: 19px; }
  .web { font-size: 19px; letter-spacing: 3.5px; }
  .person { font-size: 36px; }
  .role { font-size: 28px; font-style: italic; letter-spacing: 1px; }
  .centered { transform: translateX(-50%); text-align: center; }
  .brand {
    position: absolute; right: 18px; top: 22px;
    display: flex; flex-direction: column; align-items: center; gap: 8px;
  }
  .brand-square { width: 46px; height: 46px; background: var(--ocean); }
  .brand-name { font-size: 20px; font-weight: 800; letter-spacing: 0.5px; color: var(--ink); line-height: 1; }
  .version { position: absolute; font-size: 36px; color: var(--label); line-height: 1; }
</style>
</head>
<body>
  <section class="card card--classic">
    <div class="colour-band" role="img" aria-label="Multicolour decorative band in blue, green, plum and yellow tones"></div>
    <div class="t company" style="left:59px; top:155px;">Brushvane Pty Ltd</div>
    <div class="t detail" style="left:60px; top:195px;">58 Harbour Row</div>
    <div class="t detail" style="left:60px; top:217px;">Wellington, NEW ZEALAND</div>
    <div class="t detail" style="left:60px; top:243px;">Phone: 021-4859372</div>
    <div class="t detail" style="left:60px; top:266px;">Fax &nbsp;&nbsp;&nbsp;: 021-4859372</div>
    <div class="t detail" style="left:60px; top:289px;">Email : d.marsh@brushvane.com</div>
    <div class="t web" style="left:60px; top:311px;">www.brushvane.com</div>
    <div class="divider"></div>
    <div class="t person centered" style="left:545px; top:183px;">Daniel Marsh</div>
    <div class="t role centered" style="left:545px; top:217px;">CEO</div>
  </section>
  <div class="version" style="left:975px; top:271px;">V.1</div>

  <section class="card card--modern">
    <div class="brand">
      <div class="brand-square"></div>
      <div class="brand-name">BRUSHVANE</div>
    </div>
    <div class="t person" style="left:63px; top:141px;">Daniel Marsh</div>
    <div class="t detail" style="left:62px; top:206px;">58 Harbour Row</div>
    <div class="t detail" style="left:62px; top:228px;">Wellington, NEW ZEALAND</div>
    <div class="t detail" style="left:62px; top:256px;">Phone: 021-4859372</div>
    <div class="t detail" style="left:62px; top:278px;">Fax &nbsp;&nbsp;&nbsp;: 021-4859372</div>
    <div class="t detail" style="left:62px; top:299px;">Email : d.marsh@brushvane.com</div>
  </section>
  <div class="version" style="left:970px; top:731px;">V.2</div>
</body>
</html>
```